Company Presentation re-design.

We need to create a new 15-20 pager-presentation that will show KORVALE (travel management company) as a client-centric company with a human-to-human approach. As a start we ask a Designers to create a 3 page test presentation so we can choose the winner. who will then design the rest slides

Two main idears are to be shown on the slides:
• KORVALE is client-centric company who believes in partnership with corporate clients;
• KORVALE is a stable and trustworthy partner;

The test slides should be:

Slide (1) - Our strategy is Customer – centric strategy. KORVALE bases its business approach on the customer needs. 5 qualities that identify KORVALE as a customer-centric :
1. corporate culture, aimed at customers' changing needs
2. professional Key Account Manager (KAM)
3. Each product solution meets specific client needs.
4. innovation
5. security policy

Slide (2) - Our product solutions of clients needs
The main idea of this page is to describe our products for customers. KORVALE has 5 main products:
1. Business Travel
2. Service
3. On-line booking
4. MICE & Congress
5. Non-standard services

Slide (3)
This page shows the highlights of KORVALE support and it is shown in a cloud design now.

Attched pls find our current presentation

Dear Professionals! Please pay attantion that we updated the project by doubled the budjet! Wait for yiour grate ideas. 

Target Market(s)

Mid to top management (practically any industry), travel coordinators, procurement specialists, corporate buyers etc, travelers

Industry/Entity Type

Security

Requirements
Must have
• (1) The presentation must visualize the text above, with as little text itself as possible.
(2) We would appreciate ideas with INFOGRAPHIC
(3) Design of the presentation is up to the company logo in all variations. ( attached files).
(4) We would like to see designs that use grey, blue, orange and maroon colors - corporate colors of our logo.
Nice to have
• Infografics
Designs we like:
to brintaly.com+; zumoth.com; pelvanstudio.com; tarnowatt.co.uk (infografics)

```html
<!DOCTYPE html>
<html lang="ru">
<head>
<meta charset="utf-8">
<title>KORVALE — Стратегия ориентации на клиента</title>
<link rel="stylesheet" href="https://fonts.googleapis.com/css2?family=Oswald:wght@200;300;400&family=Open+Sans:wght@400;600&display=swap">
<style>
  :root {
    --sky-top: #c9d1dc;
    --sky-mid: #7f8fa6;
    --sky-deep: #5d6d85;
    --sky-low: #aeb1b6;
    --title-bar: #3c3d3f;
    --title-fold: #111213;
    --ring: rgba(196, 205, 218, 0.85);
    --disc: #8e8e8e;
    --shadow: #c8c8c8;
    --accent: #f58b4c;
    --white: #ffffff;
    --footer: rgba(150, 150, 150, 0.92);
    --footer-text: #4a4a4a;
  }
  * { margin: 0; padding: 0; box-sizing: border-box; }
  html, body { width: 1200px; height: 831px; overflow: hidden; }
  body { position: relative; font-family: "Oswald", sans-serif; color: var(--white); }

  .slide-backdrop {
    position: absolute; inset: 0;
    background:
      radial-gradient(ellipse 420px 260px at 540px 40px, rgba(225,231,238,0.85), transparent 70%),
      radial-gradient(ellipse 500px 260px at 1080px 260px, rgba(80,95,120,0.7), transparent 70%),
      radial-gradient(ellipse 600px 220px at 300px 640px, rgba(190,190,192,0.8), transparent 70%),
      linear-gradient(180deg, var(--sky-mid) 0%, var(--sky-deep) 45%, var(--sky-low) 80%, #9aa2ad 100%);
  }

  .slide-title {
    position: absolute; left: 66px; top: 44px; width: 554px; height: 66px;
    background: var(--title-bar);
    display: flex; align-items: center; padding-left: 54px;
    font-weight: 300; font-size: 30px; letter-spacing: 1px;
  }
  .slide-title::after {
    content: ""; position: absolute; right: 0; bottom: -15px;
    border-top: 15px solid var(--title-fold); border-left: 28px solid transparent;
  }

  .products { position: absolute; left: 0; top: 270px; width: 1200px; height: 220px; }

  .product-labels { position: absolute; top: 487px; left: 0; width: 1200px; }
  .product-label {
    position: absolute; width: 200px; text-align: center;
    font-weight: 200; font-size: 26px; line-height: 37px; text-transform: uppercase;
  }

  .slide-footer {
    position: absolute; left: 0; top: 775px; width: 1200px; height: 56px;
    background: var(--footer);
    font-family: "Open Sans", sans-serif;
  }
  .footer-brand {
    position: absolute; left: 66px; top: 6px;
    font-family: "Open Sans", sans-serif; font-weight: 400; font-size: 34px; letter-spacing: -1px;
    color: var(--white); text-transform: lowercase;
  }
  .footer-motto {
    position: absolute; left: 0; width: 1200px; top: 20px; text-align: center;
    font-size: 15px; color: var(--footer-text);
  }
  .footer-site {
    position: absolute; right: 66px; top: 20px; font-size: 15px; color: var(--footer-text);
  }
</style>
</head>
<body>
  <div class="slide-backdrop" role="img" aria-label="Размытое небо в серо-голубых тонах"></div>

  <h1 class="slide-title">СТРАТЕГИЯ ОРИЕНТАЦИИ НА КЛИЕНТА</h1>

  <svg class="products" viewBox="0 270 1200 220" width="1200" height="220" aria-label="Продукты KORVALE">
    <defs>
      <clipPath id="disc-clip" clipPathUnits="userSpaceOnUse"><circle cx="0" cy="0" r="93"/></clipPath>
    </defs>

    <!-- Business travel -->
    <g transform="translate(160 375)">
      <circle r="106" fill="var(--ring)"/>
      <g clip-path="url(#disc-clip)">
        <circle r="93" fill="var(--disc)"/>
        <polygon points="52,-24 252,176 148,240 -52,40" fill="var(--shadow)"/>
      </g>
      <rect x="-18" y="-38" width="36" height="18" rx="3" fill="none" stroke="var(--accent)" stroke-width="5"/>
      <rect x="-52" y="-24" width="104" height="64" rx="4" fill="var(--accent)"/>
      <path d="M-52 2 H52" stroke="#7a8593" stroke-width="2"/>
      <rect x="-38" y="-2" width="10" height="9" fill="none" stroke="#7a8593" stroke-width="2"/>
      <rect x="28" y="-2" width="10" height="9" fill="none" stroke="#7a8593" stroke-width="2"/>
    </g>

    <!-- MICE & Congress -->
    <g transform="translate(379 375)">
      <circle r="106" fill="var(--ring)"/>
      <g clip-path="url(#disc-clip)">
        <circle r="93" fill="var(--disc)"/>
        <polygon points="48,-46 248,154 148,244 -52,44" fill="var(--shadow)"/>
      </g>
      <rect x="-42" y="-22" width="28" height="62" fill="var(--white)" stroke="var(--accent)" stroke-width="4"/>
      <rect x="-10" y="-44" width="56" height="84" fill="var(--white)" stroke="var(--accent)" stroke-width="4"/>
      <path d="M-34 -20 V40 M-24 -20 V40 M0 -42 V40 M12 -42 V40 M30 -42 V40" stroke="var(--accent)" stroke-width="3"/>
      <rect x="-62" y="38" width="124" height="5" fill="var(--accent)"/>
    </g>

    <!-- On-line booking -->
    <g transform="translate(598 375)">
      <circle r="106" fill="var(--ring)"/>
      <g clip-path="url(#disc-clip)">
        <circle r="93" fill="var(--disc)"/>
        <polygon points="38,-64 238,136 138,264 -38,64" fill="var(--shadow)"/>
      </g>
      <rect x="-38" y="-64" width="76" height="128" rx="10" fill="var(--accent)"/>
      <rect x="-30" y="-48" width="60" height="86" rx="3" fill="var(--white)"/>
      <rect x="-8" y="-58" width="16" height="3" rx="1.5" fill="var(--white)"/>
      <circle cx="0" cy="51" r="5" fill="var(--white)"/>
      <text x="0" y="-1" text-anchor="middle" font-family="Open Sans, sans-serif" font-size="11" fill="#5a5f66">korvale</text>
    </g>

    <!-- Service -->
    <g transform="translate(817 375)">
      <circle r="106" fill="var(--ring)"/>
      <g clip-path="url(#disc-clip)">
        <circle r="93" fill="var(--disc)"/>
        <polygon points="46,-10 246,190 146,246 -32,42" fill="var(--shadow)"/>
      </g>
      <circle cx="0" cy="-62" r="10" fill="none" stroke="var(--accent)" stroke-width="5"/>
      <rect x="-5" y="-54" width="10" height="10" fill="var(--accent)"/>
      <rect x="-42" y="-56" width="14" height="8" rx="2" fill="var(--accent)" transform="rotate(-40 -35 -52)"/>
      <circle cx="0" cy="2" r="46" fill="var(--white)" stroke="var(--accent)" stroke-width="8"/>
      <g stroke="var(--accent)" stroke-width="3">
        <path d="M0 -38 V-30 M0 34 V42 M-40 2 H-32 M32 2 H40"/>
        <path d="M20 -32 L16 -25 M-20 -32 L-16 -25 M20 36 L16 29 M-20 36 L-16 29 M35 -18 L28 -14 M-35 -18 L-28 -14 M35 22 L28 18 M-35 22 L-28 18"/>
      </g>
      <path d="M0 2 L6 -26" stroke="var(--accent)" stroke-width="3"/>
      <circle cx="0" cy="2" r="4" fill="var(--accent)"/>
    </g>

    <!-- Beyond standard service -->
    <g transform="translate(1036 375)">
      <circle r="106" fill="var(--ring)"/>
      <g clip-path="url(#disc-clip)">
        <circle r="93" fill="var(--disc)"/>
        <polygon points="34,-34 234,166 166,234 -34,34" fill="var(--shadow)"/>
      </g>
      <circle r="48" fill="var(--accent)" role="img" aria-label="Глобус с материками"/>
    </g>
  </svg>

  <div class="product-labels">
    <div class="product-label" style="left:60px">Business<br>travel</div>
    <div class="product-label" style="left:279px">MICE &amp;<br>Congress</div>
    <div class="product-label" style="left:498px">On-line<br>booking</div>
    <div class="product-label" style="left:717px">Сервис</div>
    <div class="product-label" style="left:926px;width:220px">За рамками<br>стандартного<br>сервиса</div>
  </div>

  <footer class="slide-footer">
    <div class="footer-brand">korvale</div>
    <div class="footer-motto">Always learning – always growing</div>
    <div class="footer-site">www.korvale-travel.ru</div>
  </footer>
</body>
</html>
```